Optometry practice sign/banner

Modern design appeal to mix demographic, family friendly. Emphasize the importance of eye exam.
Brigh colors, green,blue, yellow,
Photo of people wearing glasses
4'x8'

" EYE EXAM, CONTACT LENS, ORTHOK, LASIK CONSULTATION, DIABETES RETINAL EXAM
DR. NORA PEL
TALVIN OPTOMETRY " Eyecare for your family"
555.762.4139
MEDICAL, VITALBASE, QRT, BRAVELINK, WALK IN WELCOME"

Target Market(s)

Family, middle age, mix demographic

Colors
33b8a4
fbee3d
cee9f5
9bcb3c

Requirements
Nice to have
• Photo of family wearing glasses.

```html
<!DOCTYPE html>
<html lang="en">
<head>
<meta charset="utf-8">
<title>Talvin Optometry – Banner</title>
<link rel="stylesheet" href="https://fonts.googleapis.com/css2?family=Open+Sans:ital,wght@0,400;0,600;0,700;1,700;1,800&family=Courgette&family=Roboto+Condensed:wght@700&display=swap">
<style>
  :root{
    --teal-deep:#24907f;
    --teal:#2a9c89;
    --teal-band:#2bb3a1;
    --brand-teal:#33b8a4;
    --yellow:#fbee3d;
    --lime:#9bcb3c;
    --sky:#cee9f5;
    --white:#ffffff;
    --ink:#333333;
    --gold:#e2b53c;
  }
  *{box-sizing:border-box;margin:0;padding:0}
  html,body{width:1200px;height:600px;overflow:hidden;background:var(--white)}
  .banner{position:relative;width:1200px;height:600px;overflow:hidden;font-family:"Open Sans",Arial,sans-serif}
  .banner__backdrop{position:absolute;inset:0}

  .brand{position:absolute;left:0;width:530px;top:30px;text-align:center;color:var(--white);font-weight:400}
  .brand__mark{display:block;width:70px;height:70px;margin:0 auto 88px;background:var(--gold)}
  .brand__name{display:block;font-size:47px;letter-spacing:2px;line-height:1}
  .brand__sub{display:block;font-size:30px;letter-spacing:3px;line-height:1.15}

  .contact{position:absolute;left:66px;top:316px;width:458px;text-align:left}
  .contact__phone{position:absolute;left:16px;top:12px;font-size:37px;font-weight:700;color:var(--white);white-space:nowrap}
  .contact__web{position:absolute;left:86px;top:60px;font-size:19px;font-weight:700;color:var(--yellow);white-space:nowrap}

  .services{position:absolute;top:438px;list-style:none;font-style:italic;font-weight:800;color:var(--white);font-size:21.5px;line-height:32px;white-space:nowrap}
  .services--a{left:66px}
  .services--b{left:286px}
  .services li::before{content:"•";color:var(--yellow);margin-right:8px;font-style:normal}

  .coverage{position:absolute;left:76px;top:550px;display:flex;align-items:center;list-style:none;color:var(--yellow);font-size:28px;font-weight:600;white-space:nowrap}
  .coverage li{display:flex;align-items:center;margin-right:16px}
  .coverage li::before{content:"";width:15px;height:15px;background:var(--lime);margin-right:10px}

  .tagline{position:absolute;left:655px;top:48px;font-family:"Courgette",cursive;color:var(--brand-teal);font-size:37px;line-height:51px}

  .walk-in{position:absolute;left:707px;top:445px;width:156px;height:156px;border-radius:50%;background:var(--lime);border:7px solid var(--white);display:flex;align-items:center;justify-content:center;text-align:center;font-family:"Roboto Condensed",Arial,sans-serif;font-weight:700;color:var(--yellow);font-size:31px;line-height:34px}

  .address{position:absolute;left:988px;top:522px;color:var(--ink);font-size:17.5px;line-height:25px}
</style>
</head>
<body>
<main class="banner">
  <svg class="banner__backdrop" width="1200" height="600" viewBox="0 0 1200 600">
    <defs>
      <linearGradient id="photoTone" x1="0" y1="0" x2="1" y2="0">
        <stop offset="0" stop-color="#d8b09a"/>
        <stop offset="0.45" stop-color="#a9c6e2"/>
        <stop offset="1" stop-color="#7fa9d4"/>
      </linearGradient>
      <linearGradient id="photoFade" x1="0" y1="0" x2="0" y2="1">
        <stop offset="0.55" stop-color="#ffffff" stop-opacity="0"/>
        <stop offset="1" stop-color="#ffffff" stop-opacity="1"/>
      </linearGradient>
      <linearGradient id="panelTone" x1="0" y1="0" x2="0" y2="1">
        <stop offset="0" stop-color="var(--teal-deep)"/>
        <stop offset="1" stop-color="var(--teal)"/>
      </linearGradient>
    </defs>
    <rect width="1200" height="600" fill="var(--white)"/>
    <g role="img" aria-label="Photo of a smiling family of three, father wearing glasses, holding a toddler in a blue dress">
      <rect x="660" y="150" width="540" height="370" fill="url(#photoTone)"/>
      <rect x="660" y="150" width="540" height="370" fill="url(#photoFade)"/>
    </g>
    <path class="curve-lime" d="M0 0 H596 C650 210 790 450 985 600 H0 Z" fill="var(--lime)"/>
    <path class="curve-yellow" d="M0 0 H565 C615 205 770 450 945 600 H0 Z" fill="var(--yellow)"/>
    <path class="panel" d="M0 0 H548 C598 205 750 450 915 600 H0 Z" fill="url(#panelTone)"/>
    <rect class="panel__band" x="0" y="316" width="640" height="94" fill="var(--teal-band)" opacity="0.55" clip-path="none"/>
    <line x1="66" y1="316" x2="500" y2="316" stroke="var(--white)" stroke-width="2"/>
    <line x1="66" y1="409" x2="524" y2="409" stroke="var(--white)" stroke-width="2"/>
  </svg>

  <div class="brand">
    <span class="brand__mark"></span>
    <span class="brand__name">TALVIN</span>
    <span class="brand__sub">OPTOMETRY</span>
  </div>

  <div class="contact">
    <p class="contact__phone">Call: 555.762.4139</p>
    <p class="contact__web">www.talvinsee.com</p>
  </div>

  <ul class="services services--a">
    <li>EYE EXAM</li>
    <li>CONTACT LENS</li>
    <li>ORTHOK</li>
  </ul>
  <ul class="services services--b">
    <li>LASIK CONSULTATION</li>
    <li>DIABETES RETINAL EXAM</li>
    <li>DRY EYE &amp; RED EYE EMERGENCY</li>
  </ul>

  <ul class="coverage">
    <li>MEDICAL</li>
    <li>VITALBASE</li>
    <li>QRT</li>
    <li>BRAVELINK</li>
  </ul>

  <p class="tagline">Eye care for<br>&nbsp;&nbsp;your family</p>

  <div class="walk-in">WALK IN<br>WELCOME</div>

  <address class="address" style="font-style:normal">4820 Marlow Ave,<br>Fernvale, CA 90417</address>
</main>
</body>
</html>
```